Site Update/Merger: TWR Dynamics

We want to take some content (not ALL the content, but only what is specified) from two or our sites and combine into one
The New Website is in Wordpress too.
The new site needs to be a nice merge between these sites:
◦ https://brontavo-works.example/
◦ https://taskmira-launch.example/
Theme/topic: this is an Engineering site
The blog must be included on the home page (maybe smaller), and also on the Systems Engineering page (maybe a little bigger, allow the user to browse through all blogs)
Instructions and visual aids:
Step 1: SEE BRIEFING IN THE PDF ATTACHED
Step 2: some pictures for your reference (referenced in the PDF)

```html
<!DOCTYPE html>
<html lang="en">
<head>
<meta charset="utf-8">
<title>TWR Dynamics</title>
<link href="https://fonts.googleapis.com/css2?family=Rubik:wght@300;400;500;600&family=Roboto:wght@400;500;700&family=Poppins:wght@400;500&display=swap" rel="stylesheet">
<style>
:root{
  --navy:#14204a;
  --navy-deep:#0f1838;
  --hero-dark:#171a30;
  --ink:#141c3c;
  --cyan:#1ab0e8;
  --blue:#0b77b8;
  --grey:#555b66;
  --light:#e6edf3;
  --foot-text:#8c9ac0;
  --white:#ffffff;
}
*{margin:0;padding:0;box-sizing:border-box}
html,body{width:671px;height:1200px;overflow:hidden;background:var(--white)}
body{position:relative;font-family:"Roboto",sans-serif;color:var(--ink)}
.abs{position:absolute}
.hero{left:0;top:0;width:671px;height:292px}
.hero-shape{position:absolute;left:0;top:0}
.site-header{left:0;top:0;width:671px;height:42px;border-bottom:1px solid rgba(255,255,255,.25)}
.brand{font-family:"Rubik",sans-serif;color:var(--white);font-size:19px;font-weight:400;left:66px;top:9px;line-height:22px}
.brand b{font-weight:600}
.nav-link{font-family:"Rubik",sans-serif;font-size:8.5px;color:var(--white);top:18px;line-height:10px;font-weight:300}
.nav-link.active{color:var(--cyan)}
.nav-underline{left:374px;top:40px;width:32px;height:2px;background:var(--white)}
.hero-title{font-family:"Rubik",sans-serif;font-weight:500;font-size:17px;line-height:18px;color:var(--white);left:64px}
.hero-title.accent{color:var(--cyan)}
.hero-text{font-size:8px;line-height:12.5px;color:var(--white);left:64px;width:290px}
.section-heading{font-family:"Rubik",sans-serif;font-size:20.5px;line-height:22px;font-weight:300}
.section-heading b{font-weight:600}
.heading-rule{height:2px;background:var(--cyan)}
.services-intro{left:100px;width:471px;top:351px;text-align:center;font-size:10px;line-height:16px;color:var(--grey)}
.panel-left{left:0;top:405px;width:336px;height:270px;background:linear-gradient(100deg,#dfe7ee 0%,#eef3f7 45%,#cfe3ef 100%)}
.panel-right{left:336px;top:405px;width:335px;height:270px;background:linear-gradient(160deg,#0a6fae 0%,#0d80c4 55%,#0b6aa8 100%)}
.badge{border-radius:50%;display:flex;align-items:center;justify-content:center}
.badge-lg{width:58px;height:58px}
.badge-sm{width:38px;height:38px;background:var(--cyan)}
.svc-title{font-family:"Rubik",sans-serif;font-size:14px;line-height:17px;font-weight:500}
.svc-sub{font-size:9px;line-height:11.5px;color:var(--grey);font-weight:400}
.item-title{font-size:9.5px;line-height:11px;font-weight:500;color:var(--ink);left:122px}
.item-text{font-size:7.5px;line-height:11px;color:#4a5160;left:122px;width:150px}
.hil-title{font-family:"Rubik",sans-serif;font-size:14px;line-height:17px;color:var(--white);left:442px;top:443px;font-weight:500}
.hil-title span{font-weight:300}
.hil-text{left:381px;top:511px;width:245px;font-size:9px;line-height:15.6px;color:var(--white)}
.blog-card{top:754px;width:175px;height:214px;background:var(--white);box-shadow:0 1px 4px rgba(0,0,0,.14)}
.blog-media{width:175px;height:115px}
.blog-date{position:absolute;left:18px;top:132px;font-size:7px;font-weight:700;color:var(--cyan);line-height:8px}
.blog-title{position:absolute;left:17px;top:142px;width:145px;font-size:9px;line-height:12.5px;font-weight:700;color:#151515}
.blog-text{position:absolute;left:17px;top:172px;width:150px;font-size:7px;line-height:11px;color:#6b6f76}
.site-footer{left:0;top:1008px;width:671px;height:152px;background:var(--navy)}
.footer-bar{left:0;top:1160px;width:671px;height:40px;background:var(--navy-deep)}
.footer-brand{font-family:"Rubik",sans-serif;color:var(--white);font-size:20px;line-height:22px;left:68px;top:1044px}
.footer-brand b{font-weight:600}
.footer-about{left:68px;top:1078px;width:130px;font-size:7.5px;line-height:11px;color:var(--foot-text)}
.col-rule{top:1008px;width:1px;height:134px;background:rgba(255,255,255,.08)}
.col-accent{width:1.5px;height:14px;background:var(--cyan);top:1040px}
.col-head{font-family:"Rubik",sans-serif;font-size:9px;line-height:10px;font-weight:500;color:var(--white);top:1042px}
.col-link{font-family:"Poppins",sans-serif;font-size:7.5px;line-height:9px;color:#c9d1e6}
.contact-line{font-family:"Poppins",sans-serif;font-size:6.5px;line-height:8px;color:#c9d1e6;left:478px}
.social{width:17px;height:17px;border:1px solid #c9d1e6;border-radius:50%;top:1096px}
.copyright{left:0;width:671px;top:1171px;text-align:center;font-size:6.5px;line-height:8px;color:#a8b2cf}
</style>
</head>
<body>

<section class="abs hero">
  <svg class="hero-shape" width="671" height="292" viewBox="0 0 671 292">
    <defs>
      <linearGradient id="heroFill" x1="0" y1="0" x2="1" y2="0.3">
        <stop offset="0" stop-color="#171a30"/>
        <stop offset="0.45" stop-color="#1b2140"/>
        <stop offset="0.7" stop-color="#2a5c86"/>
        <stop offset="1" stop-color="#4b6f96"/>
      </linearGradient>
    </defs>
    <polygon points="0,0 671,0 671,231 336,291 0,245" fill="url(#heroFill)"/>
    <rect x="330" y="42" width="341" height="240" fill="transparent" role="img" aria-label="Glowing wireframe illustration of an electric car"/>
  </svg>
</section>

<header class="abs site-header">
  <div class="abs brand"><b>TWR</b> Dynamics</div>
  <nav>
    <span class="abs nav-link active" style="left:374px">HOME</span>
    <span class="abs nav-link" style="left:446px">SERVICES
      <svg width="7" height="5" viewBox="0 0 7 5" style="margin-left:2px"><path d="M0.5 0.8 L3.5 3.8 L6.5 0.8" stroke="#fff" stroke-width="1.2" fill="none"/></svg>
    </span>
    <span class="abs nav-link" style="left:532px">CONTACT US</span>
  </nav>
  <div class="abs nav-underline"></div>
</header>

<h2 class="abs hero-title" style="top:79px">WHO WE ARE</h2>
<p class="abs hero-text" style="top:101px">A Multi-Disciplinary Consulting and Engineering Service Provider for EV and Other Industries, with a Focus on Systematic Product Development</p>
<h2 class="abs hero-title accent" style="top:151px">WHAT WE DO</h2>
<p class="abs hero-text" style="top:172px;width:275px">A team of automotive, control and mechanical engineers from different industries and backgrounds and with more than 10 years of experience that came together to provide cost effective and specialized services to your organization or team in the pursue of your projects goals</p>

<h2 class="abs section-heading" style="left:0;width:671px;text-align:center;top:313px">OUR <b>SERVICES</b></h2>
<div class="abs heading-rule" style="left:317px;top:339px;width:38px"></div>
<p class="abs services-intro">This is just a glance at the activities and projects we can contribute to. For more details, go to our services menu or contact us to have a exploratory conversation.</p>

<div class="abs panel-left" role="img" aria-label="Pale illustration of a circuit-board brain over binary digits"></div>
<div class="abs panel-right" role="img" aria-label="Blue-tinted photo of engineers at a test bench"></div>

<div class="abs badge badge-lg" style="left:57px;top:438px;background:var(--ink)">
  <svg width="30" height="30" viewBox="0 0 30 30" fill="none" stroke="#fff" stroke-width="1.3"><path d="M9 27 V21 C5 18 4 13 6 9 C9 3 18 2 22 7 C24 10 24 12 24 14 L26 18 L24 19 V22 C24 24 22 24 20 24 H18 V27"/><circle cx="16" cy="13" r="3"/><circle cx="16" cy="13" r="5.5" stroke-dasharray="2 1.6"/></svg>
</div>
<h3 class="abs svc-title" style="left:121px;top:448px">SYSTEMS ENGINEERING</h3>
<p class="abs svc-sub" style="left:122px;top:470px">Our Focus: Collaboration,<br>Accountability and Feedback</p>

<div class="abs badge badge-sm" style="left:63px;top:515px">
  <svg width="22" height="22" viewBox="0 0 22 22" fill="none" stroke="#fff" stroke-width="1.1"><circle cx="7" cy="6" r="2.5"/><circle cx="15" cy="6" r="2.5"/><path d="M2 14 C2 10 5 9 7 9 C9 9 11 10 11 12 M11 12 C11 10 13 9 15 9 C17 9 20 10 20 14"/><path d="M5 17 L9 14 L13 17 L17 14"/></svg>
</div>
<h4 class="abs item-title" style="left:122px;top:517px">Collaboration</h4>
<p class="abs item-text" style="top:530px">Working together is the only way to maximize the team’s potential</p>

<div class="abs badge badge-sm" style="left:65px;top:561px">
  <svg width="22" height="22" viewBox="0 0 22 22" fill="none" stroke="#fff" stroke-width="1.1"><path d="M8 15 C5 13 5 7 8 5 C10 3.5 12 3.5 14 5 C17 7 17 13 14 15 Z"/><path d="M8.5 17 H13.5 M9 19 H13"/><path d="M11 8 V13 M9 10 L11 8 L13 10"/></svg>
</div>
<h4 class="abs item-title" style="left:123px;top:562px">Accountability</h4>
<p class="abs item-text" style="top:574px;width:160px">Individual contributions are paramount to the team’s success</p>

<div class="abs badge badge-sm" style="left:67px;top:607px">
  <svg width="22" height="22" viewBox="0 0 22 22" fill="none" stroke="#fff" stroke-width="1.1"><rect x="4" y="4" width="14" height="10" rx="1"/><path d="M2 17 H20 L19 15 H3 Z"/><path d="M8 9 L10 11 L14 7"/></svg>
</div>
<h4 class="abs item-title" style="top:612px">Feedback</h4>
<p class="abs item-text" style="top:625px;width:160px">Clear Feedback methods are in place</p>

<div class="abs badge badge-lg" style="left:372px;top:438px;background:var(--white)">
  <svg width="40" height="30" viewBox="0 0 40 30" fill="none" stroke="#1a9ad6" stroke-width="1.2"><circle cx="9" cy="9" r="6"/><path d="M10 5 L7.5 9.5 H10.5 L8 13"/><path d="M4 24 V18 L8 14 H22 L26 18 H31 V24 Z"/><circle cx="10" cy="25" r="2.5"/><circle cx="25" cy="25" r="2.5"/><rect x="28" y="8" width="7" height="10" rx="1"/><path d="M31 18 V21 H36"/></svg>
</div>
<h3 class="abs hil-title"><span>PHYSICS-BASED MODELING</span><br>AND HARDWARE<br>IN THE LOOP</h3>
<p class="abs hil-text">From data-driven system identification to real-time math­ematical models for your simulation; we can handle that work for you. In addition, we are highly skilled on HIL testing and can support you in design and build phases to satisfy complex validation testing.</p>

<h2 class="abs section-heading" style="left:67px;top:709px;font-size:19.5px">LATEST <b style="color:var(--cyan)">BLOGS</b></h2>
<div class="abs heading-rule" style="left:70px;top:734px;width:38px"></div>

<article class="abs blog-card" style="left:67px">
  <div class="blog-media" role="img" aria-label="Photo of hands holding a tablet showing dashboards in a factory" style="background:linear-gradient(135deg,#8a96ab,#4c5a72 60%,#2b3246)"></div>
  <span class="blog-date">25 SEPTEMBER</span>
  <h3 class="blog-title">Fusce tellus Sed metus augue con­vallis et vehicula ut</h3>
  <p class="blog-text">Aonsectetuer augue nisi quis lacus Ut ac mi quis lacus mollis aliquam Curabitur iaculis</p>
</article>
<article class="abs blog-card" style="left:252px">
  <div class="blog-media" role="img" aria-label="Illustration of an electric vehicle charging plug with glowing network lines" style="background:linear-gradient(135deg,#0b2a55,#1466b0 55%,#0d3c7a)"></div>
  <span class="blog-date">15 SEPTEMBER</span>
  <h3 class="blog-title">Fusce tellus Sed metus augue con­vallis et vehicula ut</h3>
  <p class="blog-text">Aonsectetuer augue nisi quis lacus Ut ac mi quis lacus mollis aliquam Curabitur iaculis</p>
</article>
<article class="abs blog-card" style="left:437px">
  <div class="blog-media" role="img" aria-label="Photo of a hand touching a holographic car dashboard interface" style="background:linear-gradient(135deg,#0c2350,#1b5fa8 50%,#0f2f66)"></div>
  <span class="blog-date">15 SEPTEMBER</span>
  <h3 class="blog-title">Fusce tellus Sed metus augue con­vallis et vehicula ut</h3>
  <p class="blog-text">Aonsectetuer augue nisi quis lacus Ut ac mi quis lacus mollis aliquam Curabitur</p>
</article>

<footer class="abs site-footer"></footer>
<div class="abs footer-brand"><b>TWR</b> Dynamics</div>
<p class="abs footer-about">Aonsectetuer augue nisi quis lacus Ut ac mi quis lacus mollis aliquam Curabitur iaculis</p>

<div class="abs col-rule" style="left:238px"></div>
<div class="abs col-rule" style="left:345px"></div>
<div class="abs col-rule" style="left:457px"></div>
<div class="abs col-accent" style="left:238px"></div>
<div class="abs col-accent" style="left:345px"></div>
<div class="abs col-accent" style="left:458px"></div>

<h4 class="abs col-head" style="left:256px">COMPANY</h4>
<span class="abs col-link" style="left:255px;top:1062px">Home</span>
<span class="abs col-link" style="left:255px;top:1078px">Pricing</span>
<span class="abs col-link" style="left:255px;top:1095px">Features</span>
<span class="abs col-link" style="left:255px;top:1112px">traders</span>

<h4 class="abs col-head" style="left:368px">RESOURCES</h4>
<span class="abs col-link" style="left:370px;top:1062px">Blog</span>
<span class="abs col-link" style="left:370px;top:1078px">Podcast</span>
<span class="abs col-link" style="left:370px;top:1095px">About</span>
<span class="abs col-link" style="left:370px;top:1112px">Login</span>

<h4 class="abs col-head" style="left:478px">CONTACT US</h4>
<span class="abs contact-line" style="top:1062px">North America Location: Marlow Creek, SC</span>
<span class="abs contact-line" style="top:1075px">Email: info@taskmira-launch.example</span>
<span class="abs social" style="left:479px"></span>
<span class="abs social" style="left:498px"></span>
<span class="abs social" style="left:516px"></span>
<span class="abs social" style="left:535px"></span>

<div class="abs footer-bar"></div>
<p class="abs copyright">TWR DYNAMICS © 2021 ALL RIGHTS RESERVED</p>

</body>
</html>
```